Vitalquorra.com

I need a web design for a Online Wellness Center based in Chicago, IL and it's called "Vitalquorra" We provide Health risk assessment to individuals and interventions. Our portal has a Health Activity tracker where our members record health activities and aerobic miles and biometric data. Our Online wellness center tracks the participant's progress toward health goals and awards points for completed activities.
I started working on this website but the designer was not able to designer a website which describes what we do. I need a fresh look on this project. I need a very attractive, responsive website which says what we do.
These are the things we do.
1. We provide Health Risk Assessments to individuals and Co-operations
2. We Provide Free health screenings to undeserved communities
3. Assist individuals access free or affordable medications
4. We ask providers/doctors to see (or do a complete physical) one individual free of charge once a year (those individuals who are no insured and don't have money to pay from their pocket)
5. Assist patient access lab work at low cost
Our goal is to provide services that will lower the cost of care for our members.

Here is the website: www.vitalquorra.com still underdevelopment. PLEASE DO NOT COPY THIS STYLE OF WEBSITE. IT'S A BAD DESIGN AND THAT IS WHY I'M RE-DESIGNING THE SITE

Target Market(s)

Health individuals between the age of 21 to 65 Plus years old. Insured and uninsured

Industry/Entity Type

Health And Wellness

Coding

Coded - Design and coding required

Number of Pages Required

5+ page

Colors
0292cd

Requirements
Must have
• I'm still working on this websiteHere is the menu: Home, About us, Services, Health Screening, Providers, Contacts
• Please see. www.vitalquorra.com
Nice to have
• Event calender
• Upcoming Event
• Medication
• Lab assist
• Providers/Free Clinics

```html
<!DOCTYPE html>
<html lang="en">
<head>
<meta charset="utf-8">
<title>Vitalquorra – Online Wellness Center</title>
<link href="https://fonts.googleapis.com/css2?family=Open+Sans:wght@400;600;700;800&display=swap" rel="stylesheet">
<style>
:root{
  --blue:#0292cd;
  --blue-dark:#0273a6;
  --blue-deep:#025f8a;
  --green:#5cb531;
  --ink:#2d2d2d;
  --text:#6b6b6b;
  --muted:#9a9a9a;
  --line:#e3e3e3;
  --panel:#f3f3f3;
  --white:#ffffff;
}
*{margin:0;padding:0;box-sizing:border-box}
html,body{width:1200px;height:2408px;overflow:hidden}
body{font-family:"Open Sans",Arial,sans-serif;color:var(--text);background:var(--white);position:relative}
.wrap{width:1080px;margin:0 auto;position:relative}

/* header */
.site-header{height:110px;background:var(--white)}
.site-header .wrap{height:110px;display:flex;align-items:center;justify-content:space-between}
.brand{display:flex;align-items:center;gap:12px}
.brand-dot{width:38px;height:38px;border-radius:50%;background:var(--green)}
.brand-name{font-size:34px;font-weight:700;color:var(--blue);letter-spacing:-.5px}
.search{width:240px;height:34px;border:1px solid var(--line);display:flex;align-items:center;justify-content:space-between;padding:0 10px;font-size:12px;color:var(--muted)}

/* nav */
.main-nav{height:40px;background:var(--blue)}
.main-nav ul{list-style:none;display:flex;height:40px;justify-content:space-between}
.main-nav li{flex:1;text-align:center;line-height:40px;color:var(--white);font-size:12px;font-weight:700;letter-spacing:.5px}
.main-nav li.active{background:var(--green)}

/* hero */
.hero{height:502px;position:relative;background:linear-gradient(100deg,#5c8ca6 0%,#9fc3d6 35%,#dfe9ee 60%,#c7d8e1 100%)}
.hero-copy{position:absolute;left:60px;top:240px;width:430px;color:var(--white)}
.hero-copy h1{font-size:46px;font-weight:800;letter-spacing:1px;line-height:1}
.hero-copy h1 span{color:var(--green)}
.hero-copy p{margin-top:16px;font-size:14px;line-height:1.6}
.hero-arrows{position:absolute;left:60px;bottom:16px;display:flex;gap:6px}
.hero-arrows span{width:26px;height:26px;background:rgba(0,0,0,.45);display:flex;align-items:center;justify-content:center}

/* section titles */
.section-title{font-size:26px;font-weight:800;color:var(--ink);letter-spacing:.5px}
.section-title span{color:var(--blue)}

/* events */
.events{height:428px;padding-top:40px}
.events .wrap{display:flex;justify-content:space-between}
.events-list{width:700px}
.event{display:flex;gap:18px;margin-top:26px}
.event-thumb{width:110px;height:92px;flex:none;background:linear-gradient(135deg,#c9a98e,#e8d6c6 55%,#8fb4c9)}
.event h3{font-size:16px;font-weight:700;color:var(--blue)}
.event-meta{font-size:10px;color:var(--muted);margin:4px 0 6px}
.event-meta b{color:var(--blue);font-weight:600}
.event p{font-size:11px;line-height:1.65}
.calendar-box{width:330px}
.calendar{margin-top:26px;width:330px;border:1px solid #cfcfcf;background:var(--white)}
.calendar-head{height:44px;background:#4a4a4a;color:var(--white);font-size:15px;font-weight:700;text-align:center;line-height:44px;letter-spacing:1px}
.calendar table{width:100%;border-collapse:collapse;font-size:14px;font-weight:700;color:var(--ink)}
.calendar th{font-size:10px;color:var(--muted);padding:6px 0;font-weight:700}
.calendar td{text-align:center;height:30px;border-top:1px solid var(--line)}
.calendar td.off{color:#c8c8c8}
.calendar td.today{color:var(--blue)}

/* welcome */
.welcome{height:450px;background:var(--panel);padding-top:38px}
.welcome .lead{font-size:12px;color:var(--text);margin-top:6px}
.cards{display:flex;justify-content:space-between;margin-top:26px;padding:0 20px}
.card{width:316px;background:var(--white);box-shadow:0 1px 3px rgba(0,0,0,.1)}
.card-img{height:156px}
.card-img.med{background:linear-gradient(135deg,#e8e2dc,#bfb3a8 60%,#d9d1c8)}
.card-img.lab{background:linear-gradient(135deg,#6fa8c9,#cfe2ec 55%,#8fb8cf)}
.card-img.clinic{background:linear-gradient(135deg,#9fc1d6,#e9eef1 50%,#7aa4be)}
.card-body{padding:16px 18px 18px}
.card h3{font-size:14px;font-weight:700;color:var(--blue)}
.card p{font-size:11px;line-height:1.65;margin-top:8px}
.card .more{display:inline-block;margin-top:10px;font-size:10px;color:var(--green);font-weight:700}

/* what we do */
.services{height:660px;padding-top:20px}
.services .wrap{display:flex;gap:40px}
.doctor{width:320px;height:620px;flex:none;background:linear-gradient(180deg,#f4f7f9,#dfe8ee 50%,#eef2f5)}
.services-copy{padding-top:30px;width:720px}
.services-copy .rule{width:40px;height:3px;background:var(--green);margin:10px 0 18px}
.services-copy p.intro{font-size:12px;line-height:1.75}
.checklist{list-style:none;margin-top:28px}
.checklist li{display:flex;align-items:flex-start;gap:14px;font-size:13px;line-height:1.55;margin-bottom:24px;color:var(--text)}
.checklist svg{flex:none;margin-top:2px}

/* footer */
.site-footer{position:absolute;left:0;top:2190px;width:1200px;height:170px;background:var(--blue)}
.site-footer .wrap{display:flex;justify-content:space-between;padding-top:22px;color:#dff1fa}
.fcol h4{font-size:12px;font-weight:700;color:var(--white);margin-bottom:8px;letter-spacing:.5px}
.fcol p,.fcol li{font-size:10px;line-height:1.5}
.fcol ul{list-style:none}
.fcol li{margin-bottom:5px}
.fcol li span{display:block;color:var(--green);font-size:9px;line-height:1.3}
.f-about{width:220px}
.f-about .more{margin-top:6px;color:var(--white);font-weight:700}
.f-events{width:220px}
.f-contact{width:240px}
.f-news{width:280px}
.contact-row{display:flex;gap:6px;align-items:flex-start;margin-bottom:5px;font-size:10px;line-height:1.45}
.contact-row svg{flex:none;margin-top:3px}
.subscribe{display:flex;flex-direction:column;gap:8px;margin-top:10px}
.subscribe .field{height:24px;background:var(--white);width:260px;font-size:9px;color:var(--muted);padding:5px 8px}
.subscribe .btn{width:80px;height:24px;background:var(--green);color:var(--white);font-size:10px;font-weight:700;text-align:center;line-height:24px}
.bottom-bar{position:absolute;left:0;top:2360px;width:1200px;height:48px;background:var(--blue-deep)}
.bottom-bar .wrap{height:48px;display:flex;align-items:center;justify-content:space-between;font-size:10px;color:#cfe7f3}
.social{display:flex;gap:6px}
.social span{width:18px;height:18px;background:rgba(255,255,255,.25)}
</style>
</head>
<body>

<header class="site-header">
  <div class="wrap">
    <div class="brand"><span class="brand-dot"></span><span class="brand-name">Vitalquorra</span></div>
    <div class="search">Search
      <svg width="14" height="14" viewBox="0 0 14 14"><circle cx="6" cy="6" r="4.5" fill="none" stroke="#9a9a9a" stroke-width="1.6"/><line x1="9.3" y1="9.3" x2="13" y2="13" stroke="#9a9a9a" stroke-width="1.6"/></svg>
    </div>
  </div>
</header>

<nav class="main-nav">
  <div class="wrap">
    <ul>
      <li class="active">HOME</li>
      <li>ABOUT US</li>
      <li>SERVICES</li>
      <li>HEALTH SCREENING</li>
      <li>PROVIDERS</li>
      <li>CONTACTS</li>
    </ul>
  </div>
</nav>

<section class="hero" role="img" aria-label="Photo of a nurse caring for a smiling patient in a clinic bed">
  <div class="hero-copy">
    <h1>VITAL<span>QUORRA</span></h1>
    <p>Three pristine lifestyle habits will lower the risk of illness, and simple preventive care keeps you in the game for lifelong health, financial balance and stronger communities.</p>
  </div>
  <div class="hero-arrows">
    <span><svg width="8" height="12" viewBox="0 0 8 12"><polyline points="6,1 1,6 6,11" fill="none" stroke="#fff" stroke-width="2"/></svg></span>
    <span><svg width="8" height="12" viewBox="0 0 8 12"><polyline points="2,1 7,6 2,11" fill="none" stroke="#fff" stroke-width="2"/></svg></span>
  </div>
</section>

<section class="events">
  <div class="wrap">
    <div class="events-list">
      <h2 class="section-title">UPCOMING <span>EVENTS</span></h2>
      <article class="event">
        <div class="event-thumb" role="img" aria-label="Photo of a mother and child at a health event"></div>
        <div>
          <h3>Health Campus</h3>
          <div class="event-meta">Sept 15, 2015 &nbsp;|&nbsp; Written by <b>admin</b> &nbsp;|&nbsp; Comments: <b>(2)</b></div>
          <p>The mission of Vitalquorra is to reach the people and ease their disease and provide a healthy life and make a healthy and pleasant lifestyle. The mission of Vitalquorra is to reach the their disease and provide a healthy life and make a healthy and pleasant future.</p>
        </div>
      </article>
      <article class="event">
        <div class="event-thumb" role="img" aria-label="Photo of a family meeting a health advisor"></div>
        <div>
          <h3>Medication Event</h3>
          <div class="event-meta">Sept 28, 2015 &nbsp;|&nbsp; Written by <b>admin</b> &nbsp;|&nbsp; Comments: <b>(4)</b></div>
          <p>The mission of Vitalquorra is to reach the people and ease their disease and provide a healthy life and make a healthy and pleasant lifestyle. The mission of Vitalquorra is to reach the their disease and provide a healthy life and make a healthy and pleasant future.</p>
        </div>
      </article>
    </div>
    <aside class="calendar-box">
      <h2 class="section-title">EVENT <span>CALENDER</span></h2>
      <div class="calendar">
        <div class="calendar-head">SEPTEMBER 2015</div>
        <table>
          <tr><th>SUN</th><th>MON</th><th>TUE</th><th>WED</th><th>THU</th><th>FRI</th><th>SAT</th></tr>
          <tr><td class="off">30</td><td class="off">31</td><td>1</td><td>2</td><td>3</td><td>4</td><td>5</td></tr>
          <tr><td>6</td><td>7</td><td>8</td><td>9</td><td>10</td><td>11</td><td>12</td></tr>
          <tr><td>13</td><td>14</td><td class="today">15</td><td>16</td><td>17</td><td>18</td><td>19</td></tr>
          <tr><td>20</td><td>21</td><td>22</td><td>23</td><td>24</td><td>25</td><td>26</td></tr>
          <tr><td>27</td><td>28</td><td>29</td><td>30</td><td class="off">1</td><td class="off">2</td><td class="off">3</td></tr>
        </table>
      </div>
    </aside>
  </div>
</section>

<section class="welcome">
  <div class="wrap">
    <h2 class="section-title">WELCOME TO <span>VITALQUORRA</span></h2>
    <p class="lead">If you need a doctor, let our convenient center guide your care; a preventive approach for a healthier and happier community.</p>
    <div class="cards">
      <article class="card">
        <div class="card-img med" role="img" aria-label="Photo of medicine tablets and capsules"></div>
        <div class="card-body">
          <h3>MEDICATION</h3>
          <p>The mission of Vitalquorra is to reach the people and ease their disease and provide a healthy life and make a healthy and pleasant lifestyle for every member.</p>
          <span class="more">Read more »</span>
        </div>
      </article>
      <article class="card">
        <div class="card-img lab" role="img" aria-label="Photo of a lab technician working with test samples"></div>
        <div class="card-body">
          <h3>LAB ASSIST</h3>
          <p>The mission of Vitalquorra is to reach the people and ease their disease and provide a healthy life and make a healthy and pleasant lifestyle for every member.</p>
          <span class="more">Read more »</span>
        </div>
      </article>
      <article class="card">
        <div class="card-img clinic" role="img" aria-label="Photo of a group of doctors and nurses at a free clinic"></div>
        <div class="card-body">
          <h3>PROVIDERS/FREE CLINICS</h3>
          <p>The mission of Vitalquorra is to reach the people and ease their disease and provide a healthy life and make a healthy and pleasant lifestyle for every member.</p>
          <span class="more">Read more »</span>
        </div>
      </article>
    </div>
  </div>
</section>

<section class="services">
  <div class="wrap">
    <div class="doctor" role="img" aria-label="Photo of a smiling doctor in a white coat giving a thumbs up"></div>
    <div class="services-copy">
      <h2 class="section-title">WHAT <span>WE DO</span></h2>
      <div class="rule"></div>
      <p class="intro">Our mission is to create a health and wellness program that positively impacts the health and lives of all participants. These positive impacts will create healthier, happier, and more productive people. Focus will be placed on the day-to-day choices that lead to lasting lifestyle change, financial wellbeing and sustainable healthy communities.</p>
      <ul class="checklist">
        <li><svg width="18" height="18" viewBox="0 0 18 18"><polyline points="2,9 7,14 16,3" fill="none" stroke="#5cb531" stroke-width="3"/></svg>We provide Health Risk Assessments to individuals and Co-operations.</li>
        <li><svg width="18" height="18" viewBox="0 0 18 18"><polyline points="2,9 7,14 16,3" fill="none" stroke="#5cb531" stroke-width="3"/></svg>We Provide Free health screenings to underserved communities.</li>
        <li><svg width="18" height="18" viewBox="0 0 18 18"><polyline points="2,9 7,14 16,3" fill="none" stroke="#5cb531" stroke-width="3"/></svg>Assist individuals access free or affordable medications.</li>
        <li><svg width="18" height="18" viewBox="0 0 18 18"><polyline points="2,9 7,14 16,3" fill="none" stroke="#5cb531" stroke-width="3"/></svg>We ask providers/doctors to see (or do a complete physical) one individual free of charge once a year (those individuals who are not insured and don't have money to pay from their pocket).</li>
        <li><svg width="18" height="18" viewBox="0 0 18 18"><polyline points="2,9 7,14 16,3" fill="none" stroke="#5cb531" stroke-width="3"/></svg>Assist patient access lab work at low cost.</li>
      </ul>
    </div>
  </div>
</section>

<footer class="site-footer">
  <div class="wrap">
    <div class="fcol f-about">
      <p>Vitalquorra is an online wellness center that helps members track health activities, aerobic miles and biometric data, and rewards progress toward personal goals with points for every completed activity.</p>
      <p class="more">Read more »</p>
    </div>
    <div class="fcol f-events">
      <h4>RECENT EVENTS</h4>
      <ul>
        <li>Free health screening day<span>Sept 15, 2015</span></li>
        <li>Medication access workshop<span>Sept 28, 2015</span></li>
        <li>Lab assist open house<span>Oct 10, 2015</span></li>
      </ul>
    </div>
    <div class="fcol f-contact">
      <h4>CONTACT US</h4>
      <div class="contact-row"><svg width="10" height="12" viewBox="0 0 10 12"><path d="M5 0a4 4 0 0 0-4 4c0 3 4 8 4 8s4-5 4-8a4 4 0 0 0-4-4z" fill="#fff"/></svg>Address: 1420 Lakeview Ave, Suite 210, Chicago, IL 60614</div>
      <div class="contact-row"><svg width="10" height="10" viewBox="0 0 10 10"><path d="M2 0l2 2-1 2a6 6 0 0 0 3 3l2-1 2 2-2 2C4 10 0 6 0 2z" fill="#fff"/></svg>Phone: (312) 555-0148</div>
      <div class="contact-row"><svg width="11" height="8" viewBox="0 0 11 8"><rect width="11" height="8" fill="#fff"/><polyline points="0,0 5.5,4.5 11,0" fill="none" stroke="#0292cd"/></svg>Email: info@vitalquorra.com</div>
    </div>
    <div class="fcol f-news">
      <h4>NEWSLETTER</h4>
      <p>Get the latest news, event dates and health tips delivered to your inbox.</p>
      <div class="subscribe">
        <div class="field">Your email address</div>
        <div class="btn">SUBSCRIBE</div>
      </div>
    </div>
  </div>
</footer>
<div class="bottom-bar">
  <div class="wrap">
    <span>©Vitalquorra 2015 | All Rights Reserved</span>
    <div class="social"><span></span><span></span><span></span><span></span></div>
  </div>
</div>

</body>
</html>
```